TM Estates - Stone Hof Design

Looking for a double sides design, 1 side for my realestate and the other for home building. ( TM Estates on 1 side, Stone Hof card on the other Side
Side 1 - Priya Mond ~ Vex Realty logo and Company ( The Home Quarter )
Priya Mond
Priya@Priyamondhomes.example
IG - Priya_Nwt_Agent
FB - priyam
Cell - 5550193847
3874 46 St Nw

Side 2
Priya Mond
5550193847
IG - Stonehof_Nwt
Stonehofbuild@mailbox.example

Target Market(s)

Home buyers/ sellers

Industry/Entity Type

Home builders - Realestate

Contact Information for Business Card

Above

Requirements
Must have
• Black OR White background - my information -

```html
<!DOCTYPE html>
<html lang="en">
<head>
<meta charset="utf-8">
<title>TM Estates / Stone Hof — Business Cards</title>
<link rel="stylesheet" href="https://fonts.googleapis.com/css2?family=Cinzel:wght@400;600&family=Tinos&display=swap">
<style>
  :root {
    --backdrop: #141414;
    --card: #1d1d1e;
    --brand-blue: #1b74c2;
    --ink-white: #f2f2f2;
    --rule-blue: #1a5f9e;
  }
  * { margin: 0; padding: 0; box-sizing: border-box; }
  html, body { width: 1200px; height: 1059px; overflow: hidden; background: var(--backdrop); }
  .canvas { position: relative; width: 1200px; height: 1059px; }
  .card {
    position: absolute; left: 255px; width: 690px; height: 392px;
    background: var(--card); border-radius: 22px;
  }
  .card--realty { top: 89px; }
  .card--builder { top: 547px; }

  .partners { position: absolute; left: 33px; top: 38px; display: flex; gap: 18px; align-items: center; }
  .partner-name { font-family: "Tinos", serif; font-size: 13px; line-height: 1.1; color: var(--ink-white); }

  .brand { position: absolute; font-family: "Cinzel", serif; font-weight: 600; text-align: right; }
  .brand--realty { right: 34px; top: 92px; font-size: 40px; color: var(--brand-blue); letter-spacing: 1px; }
  .brand--builder { right: 32px; top: 62px; color: var(--ink-white); text-align: center; line-height: 1; }
  .brand--builder .brand-main { display: block; font-size: 38px; letter-spacing: 1px; }
  .brand--builder .brand-sub { display: block; font-size: 14px; letter-spacing: 6px; margin-top: 8px; }

  .holder-name { position: absolute; left: 34px; font-family: "Cinzel", serif; font-weight: 600; font-size: 35px; letter-spacing: 0.5px; }
  .card--realty .holder-name { top: 188px; color: var(--brand-blue); }
  .card--builder .holder-name { top: 198px; color: var(--ink-white); }

  .rule { position: absolute; left: 34px; right: 34px; height: 1.5px; background: var(--rule-blue); }
  .card--realty .rule { top: 245px; }
  .card--builder .rule { top: 257px; }

  .contact-list, .social-list { position: absolute; list-style: none; font-family: "Tinos", serif; font-size: 18px; color: var(--ink-white); }
  .contact-list { left: 34px; }
  .contact-list li, .social-list li { display: flex; align-items: center; gap: 7px; height: 25px; }
  .card--realty .contact-list { top: 263px; }
  .card--builder .contact-list { top: 270px; }
  .card--builder .contact-list li { height: 29.5px; }
  .social-list { right: 34px; align-items: flex-end; }
  .social-list li { justify-content: flex-end; }
  .card--realty .social-list { top: 314px; }
  .card--builder .social-list { top: 329px; }

  .icon { width: 13px; height: 13px; flex: none; fill: var(--brand-blue); }
  .social-dot { width: 11px; height: 11px; border: 1.6px solid var(--brand-blue); border-radius: 50%; flex: none; }
</style>
</head>
<body>
<main class="canvas">

  <section class="card card--realty">
    <div class="partners">
      <span class="partner-name">The Home<br>Quarter</span>
      <span class="partner-name">Vex<br>Realty</span>
    </div>
    <div class="brand brand--realty">TM Estates</div>
    <h1 class="holder-name">PRIYA MOND</h1>
    <div class="rule"></div>
    <ul class="contact-list">
      <li><svg class="icon" viewBox="0 0 16 16"><path d="M3.5 1l3 3-1.6 1.8c.8 1.8 2.4 3.4 4.3 4.3L11 8.5l3 3-2 2.5C6.5 13.5 2.5 9.5 1 4z"/></svg>5550193847</li>
      <li><svg class="icon" viewBox="0 0 16 16"><path d="M1 6l7-5 7 5v9H1z M2.5 7v6.5h11V7L8 11z"/></svg>Priya@Priyamondhomes.example</li>
      <li><svg class="icon" viewBox="0 0 16 16"><circle cx="8" cy="8" r="7"/><path d="M4 4c2 1 1 3 3 3s1 3-1 4M10 2c0 2 2 2 3 4" stroke="#1d1d1e" stroke-width="1.3" fill="none"/></svg>www.Priyamondhomes.example</li>
      <li><svg class="icon" viewBox="0 0 16 16"><path d="M8 0a5.5 5.5 0 0 1 5.5 5.5C13.5 10 8 16 8 16S2.5 10 2.5 5.5A5.5 5.5 0 0 1 8 0zm0 3.2a2.3 2.3 0 1 0 0 4.6 2.3 2.3 0 0 0 0-4.6z"/></svg>3874 46 St Nw</li>
    </ul>
    <ul class="social-list">
      <li><span class="social-dot"></span>Priya_Nwt_Agent</li>
      <li><span class="social-dot"></span>priyam</li>
    </ul>
  </section>

  <section class="card card--builder">
    <div class="brand brand--builder">
      <span class="brand-main">STONE HOF</span>
      <span class="brand-sub">DEVELOPMENTS</span>
    </div>
    <h2 class="holder-name">PRIYA MOND</h2>
    <div class="rule"></div>
    <ul class="contact-list">
      <li><svg class="icon" viewBox="0 0 16 16"><path d="M3.5 1l3 3-1.6 1.8c.8 1.8 2.4 3.4 4.3 4.3L11 8.5l3 3-2 2.5C6.5 13.5 2.5 9.5 1 4z"/></svg>5550193847</li>
      <li><svg class="icon" viewBox="0 0 16 16"><path d="M1 6l7-5 7 5v9H1z M2.5 7v6.5h11V7L8 11z"/></svg>Stonehofbuild@mailbox.example</li>
      <li><svg class="icon" viewBox="0 0 16 16"><circle cx="8" cy="8" r="7"/><path d="M4 4c2 1 1 3 3 3s1 3-1 4M10 2c0 2 2 2 3 4" stroke="#1d1d1e" stroke-width="1.3" fill="none"/></svg>www.stonehofbuild.example</li>
    </ul>
    <ul class="social-list">
      <li><span class="social-dot"></span>Stonehof_Nwt</li>
    </ul>
  </section>

</main>
</body>
</html>
```